Design of a promotional offer flyer required to promote low-cost websites to 1-man band businesses

I want a flyer designed - either a double-sided A5 flyer or even A4 folded into a third double-sided. The flyer is to showcase a new service - low-cost websites for 1-man-band businesses, business startups and tradesmen in England. Look at the copy, find some pix and let me know! Flyer will be printed and used as an image on my website too. Pix could be related to some of the target groups. We need to stress the simple message that websites start from £5 per week and this is an-all-in-one fee.

Target Market(s)

Tradesmen, business start ups and 1-man band businesses that want a website

Industry/Entity Type

Small Business

Contact Information for Business Card

All contact details and name of business to be confirmed shortly

Font styles to use
Serif

Requirements
Must have
• Basic messages from copy for flyer i.e. websites from £5 per week and what each client gets for that price to be included on the business card! Please read copy for the flyer.
Nice to have
• Nice background image or series of small images relevant to the target audience. Again, see list of targets from copy for flyer.
Should not have
• I don't want exact or similar design to my main business Blue Anchor Marketing. The new flyer and business card should be a different and distinct branding to that of Blue Anchor Marketing. Aimed at a more economical style, whilst looking professional, but relevant to the target audiences.

```html
<!DOCTYPE html>
<html lang="en">
<head>
<meta charset="utf-8">
<title>£5 per week websites – brochure spreads</title>
<link rel="stylesheet" href="https://fonts.googleapis.com/css2?family=Archivo+Black&family=Oswald:wght@500;700&family=Open+Sans:ital,wght@0,400;0,600;0,700;1,400;1,700&display=swap">
<style>
  :root {
    --red: #e30613;
    --red-dark: #b8050f;
    --black: #151515;
    --ink: #2b2b2b;
    --yellow: #ffd400;
    --white: #ffffff;
    --paper: #fbf8f4;
    --stage: #e4e4e4;
  }
  * { box-sizing: border-box; margin: 0; padding: 0; }
  html, body { width: 848px; height: 1200px; overflow: hidden; }
  body { background: var(--stage); font-family: "Open Sans", Arial, sans-serif; color: var(--ink); position: relative; }

  .spread { position: absolute; left: 14px; width: 820px; height: 580px; display: flex; box-shadow: 0 4px 14px rgba(0,0,0,.18); }
  .spread--outside { top: 13px; }
  .spread--inside { top: 607px; }
  .page { position: relative; width: 410px; height: 580px; overflow: hidden; background: var(--white); }
  .page + .page { border-left: 1px solid #ddd; }

  .photo { position: absolute; }
  .base-band { position: absolute; left: 0; right: 0; bottom: 0; height: 36px; background: var(--black); }
  .top-rule { position: absolute; left: 0; right: 0; top: 0; height: 9px; background: var(--red); }

  /* Back cover */
  .back { background: linear-gradient(180deg, var(--paper), #efe9e1); }
  .back .photo--painter { right: 0; top: 0; width: 180px; height: 300px; background: linear-gradient(160deg, #f4eee6, #d9cbb8 60%, #a9b7c9); }
  .back .offer-title { position: absolute; left: 34px; top: 100px; font: italic 700 15px "Open Sans", sans-serif; color: var(--black); }
  .back .offer-box { position: absolute; left: 26px; top: 128px; width: 196px; padding: 10px 12px; border: 1.5px solid #555; border-radius: 9px; background: rgba(255,255,255,.7); font-size: 11px; font-style: italic; line-height: 1.35; }
  .back .offer-box strong { display: block; font-size: 14px; font-weight: 400; margin-top: 2px; }
  .back .offer-box .cost { color: var(--red); font-weight: 700; font-size: 12px; margin-top: 4px; }

  .price-block { position: absolute; left: 0; top: 300px; width: 190px; height: 210px; background: var(--black); padding: 22px 14px; text-align: center; }
  .price-block .big { font: italic 700 58px/1 "Oswald", sans-serif; color: var(--yellow); }
  .price-block .line { font: italic 700 17px/1.2 "Oswald", sans-serif; color: var(--white); text-transform: uppercase; margin-top: 8px; }
  .price-block .line em { color: var(--yellow); font-style: italic; font-size: 21px; display: block; }

  .contact-block { position: absolute; left: 190px; top: 300px; width: 220px; height: 130px; background: var(--red); padding: 16px 16px; color: var(--white); font-size: 9.5px; font-style: italic; line-height: 1.5; }
  .contact-block .call { font: 500 20px "Oswald", sans-serif; color: var(--yellow); margin-top: 10px; letter-spacing: .5px; }
  .web-strip { position: absolute; left: 190px; top: 430px; width: 220px; height: 34px; background: var(--white); font: 600 12px "Open Sans", sans-serif; padding: 9px 0 0 62px; color: var(--black); }
  .back .base-band { height: 40px; }

  /* Front cover */
  .front { background: linear-gradient(180deg, #eeeeee, var(--white) 45%); }
  .front .photo--hero { left: 80px; top: 18px; width: 320px; height: 240px; background: linear-gradient(135deg, #c9d6e6, #6d8fb8 45%, #d9b59a 70%, #3c4f7a); border-radius: 4px; }
  .headline { position: absolute; left: 0; right: 0; top: 268px; text-align: center; font-family: "Archivo Black", sans-serif; line-height: 1.05; }
  .headline .main { display: block; font-size: 33px; color: var(--red); }
  .headline .sub { display: block; font-size: 17.5px; color: #3a3a3a; margin-top: 2px; }

  .promise-band { position: absolute; left: 0; right: 0; top: 334px; height: 92px; background: var(--red); display: flex; align-items: center; padding: 0 12px; color: var(--white); }
  .promise-band .pitch { width: 182px; flex: none; font: italic 600 12px/1.3 "Open Sans", sans-serif; padding-right: 10px; border-right: 2px solid var(--white); }
  .promise-band .pitch b { color: var(--black); white-space: nowrap; }
  .promise-band .price { padding-left: 12px; font-family: "Archivo Black", sans-serif; color: var(--yellow); line-height: 1.1; white-space: nowrap; }
  .promise-band .price .amount { display: block; font-size: 27px; }
  .promise-band .price .note { display: block; font-size: 13.5px; }

  .audience-band { position: absolute; left: 0; right: 0; top: 426px; height: 70px; background: var(--black); color: var(--white); font-size: 9.5px; line-height: 1.45; text-align: center; padding: 8px 16px; }
  .front .rule { position: absolute; left: 0; right: 0; top: 530px; height: 5px; background: var(--red); }

  /* Inside left */
  .benefits .photo--model { left: 190px; top: 16px; width: 205px; height: 180px; background: linear-gradient(150deg, #f2f2f2, #8a6a58 40%, #3a3a44 60%, #c8ccd4); border-radius: 4px; }
  .benefits h2 { position: absolute; left: 24px; top: 92px; font: 19px/1.15 "Archivo Black", sans-serif; color: var(--black); }
  .tick-list { position: absolute; left: 24px; top: 148px; width: 372px; list-style: none; font-size: 10.5px; line-height: 1.3; }
  .tick-list li { position: relative; padding-left: 18px; margin-bottom: 4px; }
  .tick-list li.narrow { width: 160px; }
  .tick-list li::before { content: ""; position: absolute; left: 3px; top: 1px; width: 5px; height: 9px; border: solid var(--red); border-width: 0 2.5px 2.5px 0; transform: rotate(40deg); }
  .tick-list b { font-weight: 700; }

  .info-band { position: absolute; left: 0; right: 0; top: 452px; height: 82px; background: var(--red); color: var(--white); text-align: center; padding-top: 12px; }
  .info-band .links { font: 20px "Archivo Black", sans-serif; }
  .info-band .links span { margin: 0 10px; }
  .info-band p { font-size: 9.5px; line-height: 1.4; }

  /* Inside right */
  .offer .photo--devices { left: 80px; top: 28px; width: 250px; height: 160px; background: linear-gradient(180deg, #dfe3e8, #4a5563 55%, #aab3bf); border-radius: 4px; }
  .offer .fee { position: absolute; left: 30px; right: 30px; top: 198px; text-align: center; font-size: 13.5px; line-height: 1.3; color: var(--black); }
  .offer .offer-title { position: absolute; left: 0; right: 0; top: 256px; text-align: center; font: 16px "Archivo Black", sans-serif; color: var(--red); }
  .offer .offer-box { position: absolute; left: 30px; right: 30px; top: 282px; border: 1.5px dashed #444; padding: 7px 10px; text-align: center; font: 12px/1.35 "Archivo Black", sans-serif; color: var(--black); background: var(--white); }
  .offer .offer-box .cost { display: block; color: var(--red); font-size: 18px; margin-top: 2px; }
  .offer .photo--technician { right: 0; top: 362px; width: 240px; height: 150px; background: linear-gradient(120deg, #f0f0f0, #b39a86 40%, #2e3540 70%, #d9dde2); }
  .call-band { position: absolute; left: 0; top: 452px; width: 200px; height: 82px; background: var(--red); color: var(--white); font: 26px "Archivo Black", sans-serif; padding: 22px 0 0 26px; }
</style>
</head>
<body>

<section class="spread spread--outside">
  <article class="page back">
    <div class="photo photo--painter" role="img" aria-label="Photo of a decorator painting a wall with a roller"></div>
    <h3 class="offer-title">Promotional Offer :</h3>
    <div class="offer-box">
      Order your new 5-page website before ............ and we'll set up a Chatterbox Page
      <strong>for FREE.</strong>
      <div class="cost">Normal Cost:<br>£97 plus VAT!</div>
    </div>
    <div class="price-block">
      <div class="big">£5</div>
      <div class="line">Per week for a<br>1-page website or<em>£10 per week</em></div>
    </div>
    <div class="contact-block">
      Email: TBC<br>
      For further information or to order.<br>
      Full terms and conditions at www. TBC.<br>
      All fees plus VAT.
      <div class="call">CALL : TBC</div>
    </div>
    <div class="web-strip">www. TBC</div>
    <div class="base-band"></div>
  </article>

  <article class="page front">
    <div class="photo photo--hero" role="img" aria-label="Photo of a smiling woman pointing at a laptop showing app icons"></div>
    <h1 class="headline">
      <span class="main">WANT A WEBSITE</span>
      <span class="sub">WITHOUT IT COSTING THE EARTH?</span>
    </h1>
    <div class="promise-band">
      <p class="pitch">Professionally-designed websites for <b>tradesmen</b>, business start-ups and <b>1-man bands</b> from only</p>
      <p class="price"><span class="amount">£5 per week</span><span class="note">&amp; NO upfront costs!</span></p>
    </div>
    <p class="audience-band">Suitable for plumbers, electricians, roofers, builders, painters and decorators, joiners, business start-ups, 1-man bands such as hairdressers, photographers, fitness instructors, window cleaners, beauticians, gardeners, odd job men, wheelie bin cleaners, IFAs or self-employed consultants.</p>
    <div class="rule"></div>
    <div class="base-band"></div>
  </article>
</section>

<section class="spread spread--inside">
  <article class="page benefits">
    <div class="top-rule"></div>
    <div class="photo photo--model" role="img" aria-label="Photo of a woman presenting a laptop with a website on screen"></div>
    <h2>Here's<br>what you get :</h2>
    <ul class="tick-list">
      <li class="narrow">Professionally-designed 1-page or 5-page website (Home, About Us, Services, Contact Us, News)</li>
      <li>Responsive design that displays properly on mobiles and tablets</li>
      <li>On-going changes and updates</li>
      <li>All text written for you</li>
      <li>Photographs (Royalty-free stock images)</li>
      <li>Professional email addresses e.g. info@yourcompany.co.uk, <b>sales@yourcompany.co.uk</b> and <b>yourname@yourcompany.co.uk</b>. We'll even set up these email addresses on your PC and laptop!</li>
      <li>Links to your social media accounts</li>
      <li>Up to 2 hours' changes each month to content, pix, and adding new pages</li>
      <li>Professional hosting for your website and email</li>
      <li>No upfront cost! Just weekly, monthly or annual invoice - you choose!</li>
    </ul>
    <div class="info-band">
      <div class="links"><span>Email: TBC</span>|<span>Visit www. TBC</span></div>
      <p>For further information or to order.<br>Full terms and conditions at www. TBC. All fees plus VAT.</p>
    </div>
    <div class="base-band"></div>
  </article>

  <article class="page offer">
    <div class="top-rule"></div>
    <div class="photo photo--devices" role="img" aria-label="Image of a website shown on desktop, laptop, tablet and phone"></div>
    <p class="fee">For an all-in fee from only £5 per week for a 1-page website or £10 per week for a 5-page website.</p>
    <h3 class="offer-title">Promotional Offer :</h3>
    <p class="offer-box">Order your new 5-page website before ............ and we'll set up a Chatterbox Page for FREE.<span class="cost">Normal Cost: £97 plus VAT!</span></p>
    <div class="photo photo--technician" role="img" aria-label="Photo of an electrician wiring a socket"></div>
    <div class="call-band">Call: TBC</div>
    <div class="base-band"></div>
  </article>
</section>

</body>
</html>
```